Home Page Design for Motor Manufacturer

Hello,
please design the homepage for a manufacturer of industry motors. I am looking for a professional, clean and minimalistic design. Since this a rather conservative industry it should get a professional look but since it is a redesign there should be some modern that gives is the modern touch of innovation.
A competitor's homepage I like is:
https://www.valtrosen.com/en/
What I like about this website:
* clean, minimal, well structured design
* mega menu
For this project please find attached the wireframes (most buttons are in German but by context and Google translate you will easily figure it out; only unclear - "Messe" means "trade exhibition"). The paddings and margins are NOT exact. Also any color of backgrounds etc. chosen is not meant to represent a real color but rather to illustrate the object and maybe show there should be some background emphasis (color or image).
Wireframes:
https: //www.filquarry. com / t / pWmeTuZa8LkiBvQx
In both wireframes the only thing that is different is the Service section. I expect from the winner both designs for this service section: one with normal cart design and one with tabs as filters to search products (find image for product categories attached)
In the header use on the left the following text:
h1: "Your competent partner for industrial engines,
-transmission and drawing parts
with more than 5000 satisfied customers "
primary button: Our products
sec. button: Download catalog
and on the right side we feature one or more product images (like putting them in a nice display together).
I also think of a solid background color or subtle gradient for the hero section.
The winner should also design an open mega menu version.
Menu items in this order:
• Home page
• Gearboxes & Motors
• Engine components
• Drawing parts
• Machines & accessories
• About us
• Contact
Also create a language switch with globe symbol and DE for Germany and EN for English above the nav plus the telephone number with icon (user dummy number +49 (0) 987650432)
Output should be in Figma, Sketch or PSD.
Fonts + color to use:
header: Proza Libre, bold, # 0171A1
body: Open Sans, regular, black
Primary accent color: # 0171A1
Text black or dark gray
background: light gray, white or shade of blue
More image resources:
https://www.filquarry.com/t/RnaHwoqPEdLu5sjv
If there are any questions please do not hesitate to ask.
Target Market(s)
B2B - anyone with industrial machinery needing small motors (not car engines)
Industry/Entity Type
Manufacturing
Number of Pages Required
1 page
Requirements
Must have
- see above
Nice to have
- see above
Should not have
- see above

```html
<!DOCTYPE html>
<html lang="en">
<head>
<meta charset="utf-8">
<title>Korvex – Industrial Motors</title>
<link href="https://fonts.googleapis.com/css2?family=Proza+Libre:wght@500;700&family=Open+Sans:wght@400;600;700&display=swap" rel="stylesheet">
<style>
:root{
  --primary:#0171A1;
  --primary-dark:#015a80;
  --accent:#F7821B;
  --ink:#1e1e1e;
  --ink-soft:#4a4a4a;
  --line:#c9d3da;
  --panel:#ececec;
  --footer:#e6e6e6;
  --white:#ffffff;
  --hero-a:#2b3640;
  --hero-b:#4d5a64;
}
*{box-sizing:border-box;margin:0;padding:0}
html,body{width:1200px;height:3912px;overflow:hidden}
body{position:relative;font-family:"Open Sans",Arial,sans-serif;color:var(--ink);background:var(--white)}
.abs{position:absolute}
h2.section-title{position:absolute;left:0;width:1200px;text-align:center;font-family:"Proza Libre",Georgia,serif;font-weight:500;font-size:30px;color:var(--ink)}

/* header */
.site-header{left:0;top:0;width:1200px;height:92px;background:var(--white);border-bottom:1px solid #e2e2e2}
.brand{left:120px;top:22px;font-family:"Open Sans",Arial,sans-serif;font-weight:700;font-size:30px;color:var(--primary);letter-spacing:1px;display:flex;align-items:center;gap:10px}
.brand .mark{width:14px;height:14px;background:var(--primary)}
.utility{right:120px;top:20px;display:flex;gap:26px;font-size:12px;color:var(--ink-soft);align-items:center}
.utility span{display:flex;align-items:center;gap:6px}
.main-nav{left:212px;top:58px;display:flex;gap:34px;font-size:13px;font-weight:600;color:var(--primary)}
.search{right:120px;top:54px;width:230px;height:22px;border-bottom:1px solid var(--line)}
.search svg{position:absolute;right:2px;top:2px}

/* hero */
.hero{left:0;top:92px;width:1200px;height:508px;background:linear-gradient(135deg,var(--hero-a),var(--hero-b) 55%,#222b32)}
.hero h1{left:0;top:48px;width:1200px;text-align:center;font-family:"Proza Libre",Georgia,serif;font-weight:700;font-size:34px;line-height:44px;color:var(--white)}
.btn-accent{background:var(--accent);color:var(--white);font-size:16px;display:flex;align-items:center;justify-content:center}
.hero .btn-accent{left:492px;top:272px;width:216px;height:52px}

.features{left:232px;top:440px;display:flex;gap:16px}
.feature{width:172px;height:168px;background:var(--primary);color:var(--white);text-align:center;padding:18px 14px}
.feature svg{display:block;margin:0 auto 8px}
.feature h3{font-size:12px;font-weight:600;margin-bottom:6px}
.feature p{font-size:10px;line-height:14px;opacity:.9}

/* products */
.tabs{left:232px;top:704px;display:flex;gap:16px}
.tab{width:172px;height:112px;border:1px solid var(--line);background:#f4f6f7;display:flex;flex-direction:column;align-items:center;justify-content:flex-end;padding-bottom:8px;font-size:13px;color:var(--ink-soft)}
.tab .thumb{width:84px;height:56px;margin-bottom:14px;background:linear-gradient(90deg,#6d7880,#c9ced2,#4b5660)}
.tab label{border-top:1px solid var(--line);width:80%;text-align:center;padding-top:4px}
.tab.is-active{background:#6a9cb7;color:var(--white)}
.tab.is-active label{border-color:rgba(255,255,255,.6)}
.filter{left:0;top:844px;width:1200px;text-align:center;font-size:16px;color:var(--ink)}
.filter b{font-weight:400;margin-right:26px}
.filter i{font-style:normal;color:#8a8a8a;margin:0 22px}

.product{width:280px}
.product .photo{position:relative;width:280px;height:212px;border:1px solid var(--line);background:radial-gradient(circle at 50% 45%,#dfe3e6,#9aa4ab 55%,#f2f2f2 56%)}
.product .caption{position:absolute;left:0;bottom:12px;width:100%;height:40px;background:rgba(1,113,161,.55);color:var(--white);font-size:16px;display:flex;align-items:center;justify-content:center}
.btn-outline{border:1.5px solid var(--primary);color:var(--ink);background:var(--white);font-size:14px;display:flex;align-items:center;justify-content:center}
.btn-solid{background:var(--primary);color:var(--white);font-size:14px;font-weight:600;display:flex;align-items:center;justify-content:center}
.product .btn-outline{width:220px;height:52px;margin:24px auto 0}

/* trade exhibition */
.exhibition-band{left:0;top:1472px;width:1200px;height:1148px;background:var(--panel)}
.fair{left:120px;width:856px;height:266px}
.fair .photo{position:absolute;left:0;top:0;width:272px;height:262px;background:linear-gradient(160deg,#f6f6f6,#b8c0c6 50%,#f4f4f4);border:1px solid #d5d5d5}
.fair h3{position:absolute;left:388px;top:10px;font-size:16px;font-weight:600}
.fair p{position:absolute;left:388px;top:44px;width:468px;font-size:12.5px;line-height:20px;color:var(--ink-soft)}
.fair .btn-outline{position:absolute;left:388px;top:196px;width:276px;height:52px;color:var(--primary);font-weight:600}
.fair .btn-solid{position:absolute;left:684px;top:196px;width:172px;height:52px}

/* about */
.about-img{background:linear-gradient(180deg,#8c8c8c,#3d3d3d)}
.about-text{left:720px;top:2760px;width:360px;font-size:14px;line-height:22px;color:var(--ink-soft)}

/* catalog band */
.catalog{left:0;top:3208px;width:1200px;height:224px;background:linear-gradient(90deg,#1c242a,#3a454d 60%,#1f282e)}
.catalog .brochure{left:48px;top:32px;width:392px;height:168px;background:linear-gradient(120deg,#f5f5f5,#d6e4ec 50%,#e9eef1)}
.catalog p{left:600px;top:28px;width:420px;font-size:14px;line-height:20px;color:#e9e9e9}
.catalog .btn-accent{left:600px;top:152px;width:220px;height:52px}

/* contact */
.contact-line{top:3522px;display:flex;align-items:center;gap:12px;font-size:13px;color:var(--ink-soft)}

/* footer */
.site-footer{left:0;top:3592px;width:1200px;height:320px;background:var(--footer)}
.site-footer .brand{left:120px;top:48px;font-size:28px}
.footer-about{left:120px;top:112px;width:300px;font-size:13px;line-height:20px;color:var(--ink-soft)}
.footer-col{top:56px;font-size:14px;line-height:28px;color:var(--ink-soft)}
.footer-col h4{font-size:15px;font-weight:700;color:var(--ink);margin-bottom:2px}
.social{left:960px;top:60px;display:flex;gap:32px}
.social span{width:22px;height:22px;border-radius:50%;background:#2a2a2a}
.copyright{left:120px;top:270px;font-size:13px;color:var(--ink-soft)}
</style>
</head>
<body>

<header class="site-header abs">
  <div class="brand abs"><span class="mark"></span>Korvex</div>
  <div class="utility abs">
    <span><svg width="12" height="12" viewBox="0 0 24 24"><path d="M6.6 10.8a15 15 0 0 0 6.6 6.6l2.2-2.2a1 1 0 0 1 1-.25 11.4 11.4 0 0 0 3.6.57 1 1 0 0 1 1 1V20a1 1 0 0 1-1 1A17 17 0 0 1 3 4a1 1 0 0 1 1-1h3.5a1 1 0 0 1 1 1c0 1.25.2 2.45.57 3.57a1 1 0 0 1-.25 1z" fill="#4a4a4a"/></svg>+49 (0) 987650432</span>
    <span><svg width="12" height="12" viewBox="0 0 24 24" fill="none" stroke="#4a4a4a" stroke-width="2"><circle cx="12" cy="12" r="10"/><path d="M2 12h20M12 2a15 15 0 0 1 0 20M12 2a15 15 0 0 0 0 20"/></svg>DE | EN</span>
  </div>
  <nav class="main-nav abs">
    <span>Home page</span><span>Gearboxes &amp; Motors</span><span>Engine components</span><span>Drawing parts</span><span>Machines &amp; accessories</span><span>About us</span><span>Contact</span>
  </nav>
</header>

<section class="hero abs" role="img" aria-label="Close-up photo of industrial gear wheels">
  <h1 class="abs">Your competent partner for<br>industrial engines,<br>transmission and drawing parts<br>with more than 5000 satisfied<br>customers</h1>
  <div class="btn-accent abs">Our Products</div>
</section>

<div class="features abs">
  <div class="feature">
    <svg width="46" height="46" viewBox="0 0 48 48" fill="none" stroke="#fff" stroke-width="2"><rect x="6" y="10" width="36" height="24"/><path d="M18 40h12M24 34v6M14 26l6-6 5 4 9-9"/></svg>
    <h3>Innovation</h3><p>Lorem ipsum dolor sit amet, consetetur sadipscing elitr, sed diam nonumy.</p>
  </div>
  <div class="feature">
    <svg width="46" height="46" viewBox="0 0 48 48" fill="none" stroke="#fff" stroke-width="2"><circle cx="16" cy="16" r="6"/><circle cx="32" cy="16" r="6"/><path d="M4 40c0-8 6-12 12-12s12 4 12 12M20 40c0-8 6-12 12-12s12 4 12 12"/></svg>
    <h3>Collaboration</h3><p>Lorem ipsum dolor sit amet, consetetur sadipscing elitr, sed diam nonumy.</p>
  </div>
  <div class="feature">
    <svg width="46" height="46" viewBox="0 0 48 48" fill="none" stroke="#fff" stroke-width="2"><rect x="10" y="6" width="28" height="36"/><path d="M16 16h16M16 24h16M16 32h10"/></svg>
    <h3>Inspection</h3><p>Lorem ipsum dolor sit amet, consetetur sadipscing elitr, sed diam nonumy.</p>
  </div>
  <div class="feature">
    <svg width="46" height="46" viewBox="0 0 48 48" fill="none" stroke="#fff" stroke-width="2"><path d="M24 38S8 28 8 18a8 8 0 0 1 16-2 8 8 0 0 1 16 2c0 10-16 20-16 20z"/><path d="M6 42h36"/></svg>
    <h3>Support</h3><p>Lorem ipsum dolor sit amet, consetetur sadipscing elitr, sed diam nonumy.</p>
  </div>
</div>

<h2 class="section-title" style="top:648px">Products</h2>
<div class="tabs abs">
  <div class="tab is-active"><div class="thumb" role="img" aria-label="Gear motor product"></div><label>Category 1</label></div>
  <div class="tab"><div class="thumb" role="img" aria-label="Planetary gearbox product"></div><label>Category 2</label></div>
  <div class="tab"><div class="thumb" role="img" aria-label="Servo motor product"></div><label>Category 3</label></div>
  <div class="tab"><div class="thumb" role="img" aria-label="Drive component product"></div><label>Category 4</label></div>
</div>
<div class="filter abs"><b>Filter:</b>All<i>|</i>Subcategory 1<i>|</i>Subcategory 2</div>

<div class="exhibition-band abs"></div>

<div class="product abs" style="left:120px;top:928px"><div class="photo" role="img" aria-label="Precision gearbox photo"><div class="caption">Product Title</div></div><div class="btn-outline">Details</div></div>
<div class="product abs" style="left:460px;top:928px"><div class="photo" role="img" aria-label="Electric motor photo"><div class="caption">Product Title</div></div><div class="btn-outline">Details</div></div>
<div class="product abs" style="left:800px;top:928px"><div class="photo" role="img" aria-label="Geared motor photo"><div class="caption">Product Title</div></div><div class="btn-outline">Details</div></div>
<div class="product abs" style="left:120px;top:1252px"><div class="photo" role="img" aria-label="Angle gearbox photo"><div class="caption">Product Title</div></div><div class="btn-outline">Details</div></div>
<div class="product abs" style="left:460px;top:1252px"><div class="photo" role="img" aria-label="Servo motor photo"><div class="caption">Product Title</div></div><div class="btn-outline">Details</div></div>
<div class="product abs" style="left:800px;top:1252px"><div class="photo" role="img" aria-label="Harmonic drive photo"><div class="caption">Product Title</div></div><div class="btn-outline">Details</div></div>

<h2 class="section-title" style="top:1636px">Trade Exhibition</h2>
<article class="fair abs" style="top:1700px">
  <div class="photo" role="img" aria-label="Harmonic gear unit exhibited at the fair"></div>
  <h3>Measure Title</h3>
  <p>Lorem Ipsum Dolor Sit Amet, Consectetur Adipiscing Elit, Sed Do Eiusmod Tempor Incididunt Ut Labore Et Dolore Magna Aliqua. Ut Enim Ad Minim Veniam, Quis Nostrud Exercitation Ullamco Laboris Nisi Ut Aliquip Ex Ea Commodo Consequat.</p>
  <div class="btn-outline">Free Ticket</div><div class="btn-solid">Details</div>
</article>
<article class="fair abs" style="top:2000px">
  <div class="photo" role="img" aria-label="Gear motor exhibited at the fair"></div>
  <h3>Measure Title</h3>
  <p>Lorem Ipsum Dolor Sit Amet, Consectetur Adipiscing Elit, Sed Do Eiusmod Tempor Incididunt Ut Labore Et Dolore Magna Aliqua. Ut Enim Ad Minim Veniam, Quis Nostrud Exercitation Ullamco Laboris Nisi Ut Aliquip Ex Ea Commodo Consequat.</p>
  <div class="btn-outline">Free Ticket</div><div class="btn-solid">Details</div>
</article>
<article class="fair abs" style="top:2300px">
  <div class="photo" role="img" aria-label="Angle gearbox exhibited at the fair"></div>
  <h3>Measure Title</h3>
  <p>Lorem Ipsum Dolor Sit Amet, Consectetur Adipiscing Elit, Sed Do Eiusmod Tempor Incididunt Ut Labore Et Dolore Magna Aliqua. Ut Enim Ad Minim Veniam, Quis Nostrud Exercitation Ullamco Laboris Nisi Ut Aliquip Ex Ea Commodo Consequat.</p>
  <div class="btn-outline">Free Ticket</div><div class="btn-solid">Details</div>
</article>

<h2 class="section-title" style="top:2648px">About Us</h2>
<div class="about-img abs" style="left:100px;top:2704px;width:288px;height:392px" role="img" aria-label="Historic black and white photo of a machine workshop"></div>
<div class="about-img abs" style="left:428px;top:2752px;width:280px;height:388px;background:linear-gradient(180deg,#6b5a48,#2e2925)" role="img" aria-label="Close-up of brass and steel gear mechanism"></div>
<p class="about-text abs">Lorem Ipsum Dolor Sit Amet, Consectetur Adipiscing Elit, Sed Do Eiusmod Tempor Incididunt Ut Labore Et Dolore Magna Aliqua. Ut Enim Ad Minim Veniam, Quis Nostrud Exercitation Ullamco Laboris Nisi Ut Aliquip Ex Ea Commodo Consequat. Duis Aute Irure Dolor Sit Amet.</p>

<section class="catalog abs" role="img" aria-label="Dark background photo of machinery">
  <div class="brochure abs" role="img" aria-label="Product catalogue brochure"></div>
  <p class="abs">Lorem Ipsum Dolor Sit Amet, Consectetur Adipiscing Elit, Sed Do Eiusmod Tempor Incididunt Ut Labore Et Dolore Magna Aliqua. Ut Enim Ad Minim Veniam, Quis Nostrud Exercitation Ullamco Laboris Nisi Ut Aliquip Ex Ea Commodo.</p>
  <div class="btn-accent abs">Download</div>
</section>

<h2 class="section-title" style="top:3470px;font-size:18px;font-family:'Open Sans',Arial,sans-serif;font-weight:400">Contact Us</h2>
<div class="contact-line abs" style="left:320px">
  <svg width="20" height="20" viewBox="0 0 24 24"><path d="M6.6 10.8a15 15 0 0 0 6.6 6.6l2.2-2.2a1 1 0 0 1 1-.25 11.4 11.4 0 0 0 3.6.57 1 1 0 0 1 1 1V20a1 1 0 0 1-1 1A17 17 0 0 1 3 4a1 1 0 0 1 1-1h3.5a1 1 0 0 1 1 1c0 1.25.2 2.45.57 3.57a1 1 0 0 1-.25 1z" fill="#0171A1"/></svg>+49 (0) 987650432
</div>
<div class="contact-line abs" style="left:700px">
  <svg width="22" height="18" viewBox="0 0 24 20" fill="none" stroke="#0171A1" stroke-width="2"><rect x="1" y="2" width="22" height="16"/><path d="M1 3l11 8 11-8"/></svg>contact@korvex.com
</div>

<footer class="site-footer abs">
  <div class="brand abs"><span class="mark"></span>Korvex</div>
  <p class="footer-about abs">Lorem ipsum dolor sit amet, consectetur adipiscing elit, sed do eiusmod tempor incididunt ut labore et dolore.</p>
  <div class="footer-col abs" style="left:508px"><h4>Company</h4>Home page<br>Gearboxes &amp; Motors<br>Engine components<br>Drawing parts<br>Machine &amp; accessories<br>About us<br>Contact</div>
  <div class="footer-col abs" style="left:732px"><h4>Help</h4>Help center<br>Contact support<br>Instructions<br>How it works</div>
  <div class="social abs"><span></span><span></span><span></span><span></span><span></span></div>
  <div class="copyright abs">© Copyright 2020. All rights reserved</div>
</footer>

</body>
</html>
```